" Factoring é um processo de fomento mercantil, no qual a empresa fomentada vende seus créditos, gerados por suas vendas a prazo, para uma empresa de factoring. É uma atividade comercial que auxilia na alavancagem dos negócios de pequenas e médias empresas, desde a prestação de serviços até a compra de ativos financeiros "

```html
<!DOCTYPE html>
<html lang="pt-BR">
<head>
<meta charset="UTF-8">
<title>Prospera Fomento Mercantil — Papelaria</title>
<link rel="stylesheet" href="https://fonts.googleapis.com/css2?family=Nunito:wght@400;700;800&display=swap">
<style>
  :root {
    --bg: #eeefee;
    --teal: #6bb4a1;
    --orange: #f08a2c;
    --paper: #ffffff;
    --ink: #7d8a86;
  }
  * { box-sizing: border-box; margin: 0; padding: 0; }
  html, body { width: 1200px; height: 1200px; overflow: hidden; }
  body {
    background: var(--bg);
    font-family: "Nunito", sans-serif;
    position: relative;
  }
  .folder-card {
    position: absolute;
    left: 110px; top: 230px;
    width: 450px; height: 680px;
    background: var(--teal);
    box-shadow: 0 10px 30px rgba(0,0,0,.12);
    display: flex; align-items: center; justify-content: center;
  }
  .brand { display: flex; flex-direction: column; line-height: 1; }
  .brand-tagline {
    font-size: 11px; font-weight: 400; letter-spacing: .5px;
    margin-bottom: 4px;
  }
  .brand-name { font-size: 56px; font-weight: 800; letter-spacing: -1px; }
  .brand--light { color: #fff; }
  .brand--teal .brand-name { color: var(--teal); }
  .brand--teal .brand-tagline { color: var(--ink); }

  .envelope {
    position: absolute;
    left: 640px; top: 230px;
    width: 450px; height: 680px;
    background: var(--paper);
    box-shadow: 0 10px 30px rgba(0,0,0,.12);
    overflow: hidden;
  }
  .envelope-flap {
    position: absolute; left: 0; top: 0; width: 100%; height: 42px;
  }
  .envelope .brand {
    position: absolute; left: 0; right: 0; top: 470px;
    align-items: center;
  }
  .envelope .brand-name { font-size: 44px; }
  .envelope .brand-tagline { font-size: 10px; }
  .contact-row {
    position: absolute; left: 24px; right: 24px; top: 572px;
    display: flex; justify-content: space-between; align-items: center;
    font-size: 11px; color: var(--ink);
    white-space: nowrap;
  }
  .contact-item { display: flex; align-items: center; gap: 5px; }
  .contact-item--email { color: var(--orange); }
  .contact-item svg { width: 11px; height: 11px; flex: none; }
  .envelope-band {
    position: absolute; left: 0; bottom: 0; width: 100%; height: 46px;
    background: var(--orange);
    color: #fff;
    display: flex; align-items: center; justify-content: center;
    font-size: 14px; font-weight: 700; letter-spacing: 1.5px;
  }
</style>
</head>
<body>
  <section class="folder-card">
    <div class="brand brand--light">
      <span class="brand-tagline">Fomento Mercantil</span>
      <span class="brand-name">Prospera</span>
    </div>
  </section>

  <section class="envelope">
    <svg class="envelope-flap" viewBox="0 0 450 42" preserveAspectRatio="none">
      <polygon points="0,0 450,0 450,42 30,42 0,18" fill="var(--teal)"/>
    </svg>
    <div class="brand brand--teal">
      <span class="brand-tagline">Fomento Mercantil</span>
      <span class="brand-name">Prospera</span>
    </div>
    <div class="contact-row">
      <span class="contact-item">
        <svg viewBox="0 0 12 12"><path d="M6 1a3.5 3.5 0 0 0-3.5 3.5C2.5 7.5 6 11 6 11s3.5-3.5 3.5-6.5A3.5 3.5 0 0 0 6 1zm0 5a1.5 1.5 0 1 1 0-3 1.5 1.5 0 0 1 0 3z" fill="var(--orange)"/></svg>
        Rua das Acácias, 120
      </span>
      <span class="contact-item contact-item--email">contato@prospera.com.br</span>
      <span class="contact-item">
        <svg viewBox="0 0 12 12"><path d="M3 1l2 2.5-1.2 1.2a7 7 0 0 0 3.5 3.5L8.5 7 11 9l-1 2C5 11 1 7 1 2z" fill="var(--orange)"/></svg>
        (11) 4000-1200
      </span>
    </div>
    <footer class="envelope-band">www.prospera.com.br</footer>
  </section>
</body>
</html>
```